Business Cards for, Telori Basuvenka - Spending Planner, employed by Clear Path Spending Planner - new business based in Brisbane Australia.

Small Business providing 'Spending Planing' services. Helping people, families, homes, businesses achieve their budgeting goals.

Motto: Counting Wisely Grows Futures

Final design should communicate financial freedom and strong positive growth.

Target Market(s)

Working Families, Finance, Retail,

Industry/Entity Type

Finance

Contact Information for Business Card

Name, Company Title
Mobile details, Email details

Logo Text

Clear Path Spending Planner - Counting Wisely Grows Futures

Font styles to use
Serif

Requirements
Must have
• Easy to read
Nice to have
• Modern Looking
Should not have
• Not too confusing to understand

```html
<!DOCTYPE html>
<html lang="en">
<head>
<meta charset="utf-8">
<title>Clear Path Spending Planner – Business Card</title>
<link rel="stylesheet" href="https://fonts.googleapis.com/css2?family=Roboto+Condensed:ital,wght@0,300;0,400;0,700;1,700&display=swap">
<style>
  :root {
    --page-bg: #ece9e4;
    --card-white: #ffffff;
    --brand-gold: #cf8f36;
    --icon-orange: #f4a03a;
    --ink: #0d0d0d;
    --text-dark: #1a1a1a;
    --tagline-white: #ffffff;
  }
  * { box-sizing: border-box; margin: 0; padding: 0; }
  html, body {
    width: 1200px; height: 1200px; overflow: hidden;
    background: var(--page-bg);
    font-family: "Roboto Condensed", "Arial Narrow", sans-serif;
  }
  .stage {
    position: relative; width: 1200px; height: 1200px;
  }
  .business-card {
    position: absolute; left: 50px; top: 288px;
    width: 1063px; height: 602px;
    transform: scale(1.0348); transform-origin: 0 0;
    background: var(--card-white);
    overflow: hidden;
    box-shadow: 0 18px 40px rgba(0,0,0,0.18);
  }
  .card-art { position: absolute; inset: 0; width: 1063px; height: 602px; }
  .brand-row {
    position: absolute; left: 0; right: 0; top: 62px; height: 56px;
    display: flex; align-items: center;
  }
  .brand-stripes {
    height: 50px;
    background: repeating-linear-gradient(to bottom, var(--brand-gold) 0 2px, transparent 2px 6px);
  }
  .brand-stripes--left { width: 76px; margin-right: 10px;
    -webkit-mask: linear-gradient(to right, transparent, #000 60%);
            mask: linear-gradient(to right, transparent, #000 60%); }
  .brand-stripes--right { flex: 1; margin-left: 14px; }
  .brand-name {
    font-weight: 700; font-size: 60px; line-height: 1;
    color: var(--brand-gold); white-space: nowrap; letter-spacing: 0.2px;
  }
  .person-name {
    position: absolute; left: 83px; top: 148px;
    font-weight: 700; font-style: italic; font-size: 52px; line-height: 1;
    color: var(--ink); letter-spacing: 1px;
  }
  .person-title {
    position: absolute; left: 83px; top: 209px;
    font-weight: 300; font-size: 38px; line-height: 1;
    color: var(--text-dark); letter-spacing: 1px;
  }
  .contact-list { position: absolute; left: 84px; top: 285px; list-style: none; }
  .contact-item { display: flex; align-items: center; height: 61px; margin-bottom: 20px; }
  .contact-icon {
    width: 61px; height: 61px; border-radius: 6px;
    background: var(--icon-orange);
    display: flex; align-items: center; justify-content: center;
    margin-right: 10px;
  }
  .contact-text { font-weight: 400; font-size: 32px; color: var(--text-dark); letter-spacing: 0.5px; }
  .tagline {
    position: absolute; left: 0; right: 0; top: 500px;
    text-align: center; font-size: 56px; line-height: 1;
    color: var(--tagline-white); letter-spacing: 0.5px;
  }
  .tagline-light { font-weight: 300; }
  .tagline-bold { font-weight: 700; }
</style>
</head>
<body>
<main class="stage">
  <section class="business-card" aria-label="Clear Path Spending Planner business card">
    <svg class="card-art" viewBox="0 0 1063 602" aria-hidden="false">
      <defs>
        <radialGradient id="coinGlow" cx="0.6" cy="0.55" r="0.6">
          <stop offset="0" stop-color="#c99b5a"/>
          <stop offset="0.55" stop-color="#e8cfa7"/>
          <stop offset="1" stop-color="#ffffff" stop-opacity="0"/>
        </radialGradient>
      </defs>
      <rect class="coin-photo" x="420" y="240" width="580" height="200" fill="url(#coinGlow)"
            role="img" aria-label="Photo of gold coin stacks rising in height from left to right"/>
      <path class="bottom-band" fill="var(--brand-gold)"
            d="M0 408 C150 450 350 475 520 470 C760 462 950 420 1063 375 L1063 602 L0 602 Z"/>
      <path class="growth-swoosh" fill="var(--ink)"
            d="M200 460 C500 478 850 430 1063 295 L1063 375 C950 420 760 462 520 470 C400 474 300 470 200 460 Z"/>
      <path class="growth-arrow" fill="none" stroke="var(--brand-gold)" stroke-width="5" stroke-linecap="round"
            d="M540 468 C750 458 905 418 1006 356"/>
      <polygon class="growth-arrow-head" fill="var(--brand-gold)" points="988,346 1018,341 1010,370"/>
    </svg>

    <div class="brand-row">
      <span class="brand-stripes brand-stripes--left"></span>
      <span class="brand-name">Clear Path Spending Planner</span>
      <span class="brand-stripes brand-stripes--right"></span>
    </div>

    <h1 class="person-name">TELORI BASUVENKA</h1>
    <p class="person-title">SPENDING PLANNER</p>

    <ul class="contact-list">
      <li class="contact-item">
        <span class="contact-icon">
          <svg width="38" height="38" viewBox="0 0 24 24" aria-hidden="true">
            <path fill="#fff" d="M6.6 10.8a15.1 15.1 0 0 0 6.6 6.6l2.2-2.2a1 1 0 0 1 1-.25 11.4 11.4 0 0 0 3.6.57 1 1 0 0 1 1 1V20a1 1 0 0 1-1 1A17 17 0 0 1 3 4a1 1 0 0 1 1-1h3.5a1 1 0 0 1 1 1c0 1.25.2 2.45.57 3.57a1 1 0 0 1-.25 1z"/>
          </svg>
        </span>
        <span class="contact-text">+61 412 806 354</span>
      </li>
      <li class="contact-item">
        <span class="contact-icon">
          <svg width="40" height="40" viewBox="0 0 40 40" aria-hidden="true">
            <text x="20" y="31" text-anchor="middle" font-family="Roboto Condensed, sans-serif" font-size="36" font-weight="400" fill="#fff">@</text>
          </svg>
        </span>
        <span class="contact-text">telori@clearpathsp.com</span>
      </li>
    </ul>

    <p class="tagline"><span class="tagline-light">COUNTING WISELY</span> <span class="tagline-bold">GROWS FUTURES</span></p>
  </section>
</main>
</body>
</html>
```